Banner Ad Design Project

We are re-branding our energy management company called 'Voltaris'. We sell Energy Management Information Software and are currently positioned as a very technical organization. While we are always going to be very technical we want to shift away from telling people about the power of our software and become a more customer centric organization focusing on how energy management can solve many of your organizations problems. The final design should be modern and simple, as we are taking something very technical and complicated and trying to sell it. We need 4 banners created for our site www.voltaris-example.com which rotate across the top. They all need to be different and easily editable (preferably Photoshop)as we change marketing campaigns, the text needs to be editable.

The Size of the banners are 940 pixels by 250 pixels.
Updates

Thank you so much to everyone for you questions and for the few designs I have received. I am very new at this so please if there are things I can do to help better convey my design needs please let me know. Many people have asked for the Text to do on the banners. Here is what I have come up with for the 4 banners.

Banner 1

Maintain high building standards
                - With lower energy costs

Banner 2
Energy Reporting Requirements
                - Made effortless

Banner 3
Presenting Carl Benson, President of QELTRA, June 19th
- The future of Ontario’s power market

Banner 4
Working with utilities to develop and execute successful Energy Conservation Programs

As well we are working on re-branding ourselves so the website at this point does not convey the look and feel we are looking to go with. The attached files, especially the brochure and business card, convey the look and feel I am looking fore much better!

Reason: Need to check with the rest of my team to make final decision. Keep submitting designs, Thanks!

Industry/Entity Type

Marketing

Requirements
Must have
• The size needs to be 940 by 250 pixels. They need to contain the green color indicated in the 'Voltaris branding design features' document.

Needs to be consistent withe the look and feel of the brochure, PowerPoint and business card attached.

The integration of the 'Voltaris Head' and other similar graphics into the banners.
Should not have
• The look and feel of our current website

```html
<!DOCTYPE html>
<html lang="en">
<head>
<meta charset="utf-8">
<title>Voltaris Banners</title>
<link href="https://fonts.googleapis.com/css2?family=Arvo:wght@700&family=Montserrat:wght@300&display=swap" rel="stylesheet">
<style>
  :root {
    --brand-green: #00582f;
    --brand-green-soft: #0d6a3d;
    --accent-green: #8dc63f;
    --white: #ffffff;
    --page-bg: #ffffff;
  }
  * { margin: 0; padding: 0; box-sizing: border-box; }
  html, body {
    width: 1200px; height: 1000px; overflow: hidden;
    background: var(--page-bg);
  }
  .canvas { position: relative; width: 1200px; height: 1000px; }
  .banner {
    position: absolute; left: 224px; width: 752px; height: 200px;
    background: var(--brand-green); overflow: hidden;
  }
  .banner--building { top: 50px; }
  .banner--reporting { top: 283px; }
  .banner--speaker { top: 517px; }
  .banner--utilities { top: 750px; }

  .banner__art {
    position: absolute;
    background: linear-gradient(180deg, var(--brand-green-soft), var(--brand-green));
    border-radius: 4px;
  }
  .banner--building .banner__art { left: 552px; top: 20px; width: 150px; height: 148px; }
  .banner--reporting .banner__art { left: 552px; top: 20px; width: 152px; height: 161px; }
  .banner--speaker .banner__art {
    left: 548px; top: 23px; width: 168px; height: 165px;
    background: rgba(255,255,255,0.92);
  }
  .banner--utilities .banner__art { left: 552px; top: 22px; width: 154px; height: 178px; border-radius: 4px 4px 0 0; }

  .rule {
    position: absolute; left: 32px; width: 476px; height: 0;
    border-top: 1.5px dashed var(--white);
  }
  .headline {
    position: absolute; left: 32px;
    font-family: "Arvo", "Rockwell", serif; font-weight: 700;
    font-size: 26px; line-height: 29px; letter-spacing: 0.4px;
    color: var(--white); white-space: nowrap;
  }
  .headline sup { font-size: 12px; vertical-align: 11px; line-height: 0; }
  .tagline {
    position: absolute;
    font-family: "Montserrat", sans-serif; font-weight: 300;
    font-size: 20px; line-height: 24px; color: var(--accent-green);
    white-space: nowrap;
  }
</style>
</head>
<body>
<main class="canvas">

  <section class="banner banner--building">
    <div class="banner__art" role="img" aria-label="Illustration of energy icons linked by dashed lines to a classical building"></div>
    <div class="rule" style="top:24px"></div>
    <h2 class="headline" style="top:36px">Maintain high building standards</h2>
    <p class="tagline" style="top:68px; right:245px">With lower energy costs</p>
    <div class="rule" style="top:105px"></div>
  </section>

  <section class="banner banner--reporting">
    <div class="banner__art" role="img" aria-label="Illustration of renewable energy icons feeding a reporting dashboard with charts"></div>
    <div class="rule" style="top:24px"></div>
    <h2 class="headline" style="top:36px">Energy Reporting Requirements</h2>
    <p class="tagline" style="top:68px; right:262px">Made effortless</p>
    <div class="rule" style="top:105px"></div>
  </section>

  <section class="banner banner--speaker">
    <div class="banner__art" role="img" aria-label="Map of Ontario with transmission towers"></div>
    <div class="rule" style="top:24px"></div>
    <h2 class="headline" style="top:36px">Presenting Carl Benson,<br>President of QELTRA, June 19<sup>th</sup></h2>
    <p class="tagline" style="top:95px; left:67px">The future of Ontario’s power market</p>
    <div class="rule" style="top:129px"></div>
  </section>

  <section class="banner banner--utilities">
    <div class="banner__art" role="img" aria-label="Illustration of resource icons linked to an outlined head with a light bulb inside"></div>
    <div class="rule" style="top:24px"></div>
    <h2 class="headline" style="top:36px">Working with utilities to develop<br>and execute successful Energy</h2>
    <p class="tagline" style="top:95px; right:286px">Conservation Programs</p>
    <div class="rule" style="top:129px"></div>
  </section>

</main>
</body>
</html>
```